Bridal Pastry Trade Institute Website Homepage Revision

I need the "homepage" to the new Coastal Bridal Pastry Trade Institute to reworked. The current homepage is dull. It needs the attention of a professional graphic artist so it delivers a professionally finished feel and look. I have included the current URL for your viewing (builds.vornelt.com/coastal-pastry/cms/ ) to see where we are in the development phase. The elements on the homepage are all necessary and the colors are correct. I have also included the original Word document for the page (you can extract the RGB values and images from the doc). To be clear, I am not looking to recreate all the web pages, just the homepage. It needs to be responsive and stretched.

Target Market(s)

All bakers who sell wedding cakes in the United States

Number of Pages Required

1 page

Font styles to use
Other font styles liked:
• see the Word Document

Requirements
Must have
• It must have the elements already in the original mock up. That includes the colors and fonts.

```html
<!DOCTYPE html>
<html lang="en">
<head>
<meta charset="utf-8">
<title>Coastal Bridal Pastry Trade Institute</title>
<link href="https://fonts.googleapis.com/css2?family=Lora:ital,wght@0,400;0,700;1,400&display=swap" rel="stylesheet">
<style>
:root{
  --teal:#00c7c7;
  --white:#ffffff;
  --ink:#1d1d1d;
  --gold:#ffb700;
  --mist:#d3e0e0;
  --card-shadow:rgba(0,0,0,0.10);
}
*{margin:0;padding:0;box-sizing:border-box}
html,body{width:1200px;height:1200px;overflow:hidden;background:var(--white);font-family:'Lora',Georgia,serif}
.page{position:relative;width:1200px;height:1200px;overflow:hidden}
.hero{position:absolute;left:0;top:0;width:1200px;height:424px;background:var(--teal)}
.hero-title{position:absolute;left:0;top:-12px;width:1200px;text-align:center;color:var(--white);font-weight:700;font-size:34px;letter-spacing:0.5px;text-shadow:0 2px 4px rgba(0,0,0,0.25)}
.path{position:absolute;top:80px;width:240px;text-align:center;color:var(--white)}
.path-icon{display:block;margin:0 auto;width:108px;height:108px}
.path-label{margin-top:33px;font-size:22px;line-height:33px}
.path-label b{font-weight:700}
.path-link{margin-top:28px;display:flex;align-items:center;justify-content:center;gap:14px;font-size:16px}
.path-link span.rule{display:block;width:30px;height:1px;background:var(--white)}
.path-link a{color:var(--white)}
.card{position:absolute;top:482px;width:264px;height:592px;background:var(--white);border-radius:12px;box-shadow:0 8px 22px var(--card-shadow);overflow:hidden;text-align:center}
.card-photo{height:243px}
.card-text{padding:36px 18px 0;font-size:21px;line-height:33.5px;font-style:italic;color:var(--ink)}
.card-text b{font-style:normal;font-weight:700;font-size:24px}
.card-btn{position:absolute;left:44px;top:510px;width:171px;height:46px;border-radius:23px;background:var(--gold);color:var(--ink);font-weight:700;font-size:19px;line-height:46px;text-decoration:none}
.method{position:absolute;left:0;top:1136px;width:1200px;height:64px;background:var(--mist)}
.method-title{position:absolute;left:0;top:38px;width:1200px;text-align:center;font-weight:700;font-size:36px;letter-spacing:9px;color:var(--ink);white-space:nowrap}
</style>
</head>
<body>
<div class="page">
  <section class="hero">
    <h1 class="hero-title">WE’RE REWRITING THE BOOK FOR SELLING</h1>

    <div class="path" style="left:143px">
      <svg class="path-icon" viewBox="0 0 108 108" fill="none" stroke="#fff" stroke-width="3"><circle cx="54" cy="54" r="52"/><path d="M40 50c0-12 6-18 14-18s14 6 14 18c0 10-6 18-14 18s-14-8-14-18z" stroke-width="2"/><path d="M40 46c6-2 12-8 14-12 4 6 10 10 14 12" stroke-width="2"/><path d="M46 72l8 4 8-4-2 6h-12z" stroke-width="2"/></svg>
      <p class="path-label">I’m <b>NEW</b> to<br>Selling Wedding<br>Cakes</p>
      <div class="path-link"><span class="rule"></span><a href="#">Click Here</a><span class="rule"></span></div>
    </div>

    <div class="path" style="left:369px">
      <svg class="path-icon" viewBox="0 0 108 108" fill="none" stroke="#fff" stroke-width="3"><circle cx="54" cy="54" r="52"/><g stroke-width="2"><rect x="33" y="60" width="42" height="12" rx="2"/><rect x="37" y="50" width="34" height="10" rx="2"/><rect x="42" y="42" width="24" height="8" rx="2"/><path d="M54 40c-4-4-6-8-2-9 1 0 2 1 2 2 0-1 1-2 2-2 4 1 2 5-2 9z"/><path d="M33 66c7 3 14-3 21 0s14 3 21 0"/></g></svg>
      <p class="path-label">I Want to<br><b>MAINTAIN</b><br>my sales</p>
      <div class="path-link"><span class="rule"></span><a href="#">Click Here</a><span class="rule"></span></div>
    </div>

    <div class="path" style="left:599px">
      <svg class="path-icon" viewBox="0 0 108 108" fill="none" stroke="#fff" stroke-width="3"><circle cx="54" cy="54" r="52"/><g stroke-width="2.5"><rect x="34" y="60" width="10" height="14"/><rect x="48" y="50" width="10" height="24"/><rect x="62" y="40" width="10" height="34"/><path d="M34 52l14-14M42 37h7v7"/></g></svg>
      <p class="path-label">I’m Eager to<br><b>BOOST</b> My Sales<br>and Profits</p>
      <div class="path-link"><span class="rule"></span><a href="#">Click Here</a><span class="rule"></span></div>
    </div>

    <div class="path" style="left:825px">
      <svg class="path-icon" viewBox="0 0 108 108" fill="none" stroke="#fff" stroke-width="3"><circle cx="54" cy="54" r="52"/><path d="M54 34l6 13 14 1-11 9 4 14-13-8-13 8 4-14-11-9 14-1z" stroke-width="2.5"/></svg>
      <p class="path-label">I’m Ready to<br><b>DOMINATE</b> My<br>Market Area</p>
      <div class="path-link"><span class="rule"></span><a href="#">Click Here</a><span class="rule"></span></div>
    </div>
  </section>

  <article class="card" style="left:174px">
    <div class="card-photo" role="img" aria-label="Three smiling pastry chefs in white hats, one holding a red cake bakers book" style="background:linear-gradient(135deg,#2b3550,#dfe2ea 55%,#a8213a)"></div>
    <p class="card-text"><b>Become</b> the “World’s Greatest.” You’ll have an atmosphere sa spe-cial, brides won’t think of using anyone but you!</p>
    <a class="card-btn" href="#">More</a>
  </article>

  <article class="card" style="left:466px">
    <div class="card-photo" role="img" aria-label="Surprised woman beside a chalk question mark on a blackboard" style="background:linear-gradient(90deg,#3a2c28,#2b2b2b 55%,#6a6a6a)"></div>
    <p class="card-text"><b>Peek</b> at a very effective psychological sales riddle called “The insecurity Gap.”</p>
    <a class="card-btn" href="#">More</a>
  </article>

  <article class="card" style="left:759px">
    <div class="card-photo" role="img" aria-label="Blonde woman's portrait half in colour, half in black and white" style="background:linear-gradient(90deg,#e8c79a,#d9a580 45%,#9a9a9a 55%,#d8d8d8)"></div>
    <p class="card-text"><b>Discover</b> a sales growth secret that reveals the “Two Faces of Your Wedding Cake Business.”</p>
    <a class="card-btn" href="#">More</a>
  </article>

  <section class="method">
    <h2 class="method-title">How Getting to the Method Brings Buyers Get MORE</h2>
  </section>
</div>
</body>
</html>
```